Rovema Tyres Business Card Design

Business of 10 years, looking for a new business card. It will be double sided. Size when cut is approx. 90x55mm.
Logo will be provided. Use the colours: green, blue, white, (black if necessary).
Either on white, or grey background.

Information to put on card:
On the front:
[the logo] on the top left

Owen Pardy
47 Hollister St Dunmorrow
Phone: (02) 9671 2043
Fax: (02) 9671 3358
Email: rovemaowen@mailvista.example

On the back:
Have a light green background with faint artistic pattern, or just a plain light green.

What we do:
- Tyres
- Wheels
- Wheel Alignments
- Car Service

At the bottom of back put this bible verse:
Jesus said: "Whoever has my commands and keeps them is the one who loves me. The one who loves me will be loved by my Father, and I too will love them and show myself to them.”

Target Market(s)

Everyone

Industry/Entity Type

Business

Contact Information for Business Card

On the front:

Owen Pardy
47 Hollister St Dunmorrow
Phone: (02) 9671 2043
Fax: (02) 9671 3358

On the back:

What we do:
- Tyres
- Wheels
- Wheel Alignments
- Car Service

On the front:

Owen Pardy
47 Hollister St Dunmorrow
Phone: (02) 9671 2043
Fax: (02) 9671 3358

On the back:

What we do:
- Tyres
- Wheels
- Wheel Alignments
- Car Service

Designer can recommend colours, other than the ones I have chosen.

Font styles to use
Serif

Colors
9bcb3c
acd037
33a6d7
85cae6
5c5c5c
757575
474747
ffffff
fbfbfb

Requirements
Must have
• Business of 10 years, looking for a new business card. It will be double sided. Size when cut is approx. 90x55mm.
• Logo will be provided. Use the colours: green, blue, white, (black if necessary).
• Either on white, or grey background.
• Information to put on card:
• On the front:
• [the logo] on the top left
• Owen Pardy
• 47 Hollister St Dunmorrow
• Phone: (02) 9671 2043
• Fax: (02) 9671 3358
• Email: rovemaowen@mailvista.example
• On the back:
• Have a light green background with faint artistic pattern, or just a plain light green.
• What we do:
• - Tyres
• - Wheels
• - Wheel Alignments
• - Car Service
• At the bottom of back put this bible verse:
• Jesus said: "Whoever has my commands and keeps them is the one who loves me. The one who loves me will be loved by my Father, and I too will love them and show myself to them.”
Nice to have
• Elegant borders (think art deco)
Should not have
• Expletives (no one's going to put that there right ? )

```html
<!DOCTYPE html>
<html lang="en">
<head>
<meta charset="utf-8">
<title>Rovema Tyres – Business Card Back</title>
<link rel="stylesheet" href="https://fonts.googleapis.com/css2?family=Electrolize&display=swap">
<style>
  :root {
    --card-green: #acd037;
    --emblem-green: #9fb83b;
    --ink: #474747;
  }
  html, body {
    margin: 0;
    padding: 0;
    width: 1200px;
    height: 734px;
    overflow: hidden;
    background: var(--card-green);
  }
  .card-back {
    position: relative;
    width: 1200px;
    height: 734px;
    background: var(--card-green);
    font-family: "Electrolize", "Century Gothic", sans-serif;
    color: var(--ink);
  }
  .emblem-area {
    position: absolute;
    left: 115px;
    top: 42px;
    width: 970px;
    height: 504px;
    background: radial-gradient(ellipse 25% 50% at 50% 50%, var(--emblem-green) 0%, var(--emblem-green) 55%, var(--card-green) 100%);
  }
  .services {
    position: absolute;
    left: 0;
    right: 0;
    top: 276px;
    margin: 0;
    text-align: center;
    font-size: 36px;
    font-weight: 400;
    line-height: 44px;
    white-space: pre;
  }
  .verse {
    position: absolute;
    left: 0;
    right: 0;
    top: 573px;
    margin: 0;
    text-align: center;
    font-size: 29px;
    font-weight: 400;
    line-height: 39px;
  }
</style>
</head>
<body>
<main class="card-back">
  <div class="emblem-area" role="img" aria-label="Faint tyre emblem with tread edge and side wings behind the services line"></div>

  <p class="services">Tyres  |  Wheels  |  Wheel Alignments  |  Car Service</p>

  <p class="verse">Jesus said: "Whoever has my commands and keeps them is the<br>
  one who loves me. The one who loves me will be loved<br>
  by my Father, and I too will love them and show myself to them.”</p>
</main>
</body>
</html>
```